TovaLamarpe - Israeli Mental Health Website

We are developing an Israeli website for mental health. The website will be both in English and in Hebrew. We have a logo and would like a website design based on the logo and the logos colors (attached).

Attached is a doc that contains the website requirements.

We would like to have an icon for each of the sidebar categories, an image for each of the pages (including each of the sidebar category pages).

Target Market(s)

Adults 18-80

Industry/Entity Type

Mental Health

Number of Pages Required

5+ page

Font styles to use
Sans Serif

Colors

Designer to choose colors to be used in the design.

```html
<!DOCTYPE html>
<html lang="en">
<head>
<meta charset="utf-8">
<title>TovaLamarpe – Mental Health Support</title>
<link href="https://fonts.googleapis.com/css2?family=Open+Sans:wght@400;600;700&family=Montserrat:wght@500;800&display=swap" rel="stylesheet">
<style>
:root{
  --blue:#0a55a0;
  --blue-deep:#0050a0;
  --blue-bright:#2b8de0;
  --green:#4fae3f;
  --ink:#222;
  --muted:#444;
  --footer:#231f1e;
  --white:#fff;
}
*{box-sizing:border-box;margin:0;padding:0}
html,body{width:1200px;height:2250px;overflow:hidden}
body{position:relative;font-family:"Open Sans",sans-serif;color:var(--ink);background:var(--white)}
.abs{position:absolute}
a{color:inherit;text-decoration:none}

/* header */
.brand{left:87px;top:30px;width:170px;text-align:center;font-weight:700;font-size:24px;color:var(--blue)}
.brand-dot{display:block;width:44px;height:44px;border-radius:50%;border:4px solid var(--green);margin:0 auto 8px}
.topbar{left:545px;top:0;width:560px;height:36px;background:#f6f6f6;display:flex;align-items:center;gap:22px;padding-left:68px;font-size:14.5px;color:#333}
.topbar span{display:flex;align-items:center;gap:7px}
.social{display:flex;gap:14px;align-items:center}
.social i{display:block;width:14px;height:14px;border-radius:50%;background:#222}
.social i.on{width:24px;height:24px;background:var(--blue)}
.nav{left:347px;top:60px;display:flex;gap:29px;font-size:15px;font-weight:600;color:#222;letter-spacing:.3px}
.nav .active{color:var(--blue-bright);text-decoration:underline}
.donate{left:928px;top:54px;width:108px;height:36px;border-radius:18px;background:var(--green);color:#fff;font-size:14px;font-weight:600;display:flex;align-items:center;justify-content:center}
.lang{left:1054px;top:58px;width:57px;height:28px;border-radius:14px;border:2px solid var(--green);color:var(--green);font-size:11px;font-weight:600;display:flex;align-items:center;justify-content:center;gap:6px}

/* hero */
.sidebar{left:0;top:107px;width:384px;height:528px;background:var(--blue-deep);padding-top:15px}
.cat{position:relative;margin-left:88px;width:296px;display:flex;align-items:center;gap:10px;padding:0 16px;color:#fff;font-size:15.5px;line-height:19px;min-height:35px}
.cat.two{min-height:54px}
.cat.active{background:#1c71c9;height:39px;margin-bottom:0}
.cat svg{flex:none;width:22px;height:22px;stroke:#fff;fill:none;stroke-width:1.6}
.cat .arrow{position:absolute;right:12px;width:18px;height:18px}
.hero-photo{left:396px;top:107px;width:804px;height:528px;background:linear-gradient(120deg,#31505a 0%,#46606a 45%,#6d757a 75%,#3b3a3c 100%)}
.hero-shade{left:396px;top:107px;width:804px;height:528px;background:linear-gradient(90deg,rgba(10,30,50,.55),rgba(10,30,50,.1))}
.hero-title{left:478px;top:245px;font-family:"Montserrat",sans-serif;font-weight:800;font-size:47px;line-height:48px;color:var(--blue-bright)}
.hero-text{left:478px;top:356px;width:430px;font-family:"Montserrat",sans-serif;font-weight:500;font-size:15.5px;line-height:24px;color:#fff}
.hero-btn{left:478px;top:454px;width:360px;height:35px;border-radius:18px;background:var(--green);color:#fff;font-size:13.5px;font-weight:600;display:flex;align-items:center;justify-content:center}

/* about */
.about-title{left:0;top:702px;width:1200px;text-align:center;font-size:38px;font-weight:700;color:var(--blue)}
.about-title em{font-style:normal;color:var(--green)}
.about-text{left:160px;top:768px;width:880px;text-align:center;font-size:14.6px;line-height:21px;color:var(--ink)}
.about-text p+p{margin-top:21px}
.btn{height:34px;border-radius:17px;color:#fff;font-size:13.5px;font-weight:600;display:flex;align-items:center;justify-content:center}
.btn.blue{background:var(--blue)}
.btn.green{background:var(--green)}

/* cards */
.card-photo{width:500px;height:260px;border:3px solid #fff;outline:1px solid #ddd}
.card-box{width:451px;height:169px;background:#fff;box-shadow:0 6px 10px rgba(0,0,0,.08);padding:22px 24px 0}
.card-box h3{font-size:19px;font-weight:700;color:var(--blue);letter-spacing:.3px}
.card-box p{margin-top:9px;font-size:13.6px;line-height:19px;color:var(--muted)}
.card-box .btn{position:absolute;left:25px;top:127px}

/* footer */
.footer{left:0;top:1920px;width:1200px;height:291px;background:var(--footer)}
.foot-brand{left:87px;top:1998px;width:217px;text-align:center;color:var(--blue-bright);font-weight:700;font-size:28px}
.foot-brand .brand-dot{width:56px;height:56px;border-width:5px;margin-bottom:12px}
.foot-h{font-size:16px;font-weight:700;color:var(--green);letter-spacing:.5px}
.contact{left:365px;top:1980px;color:#fff;font-size:14.5px;line-height:21px}
.contact li{list-style:none;display:flex;gap:14px;margin-top:14px}
.contact li+li{margin-top:17px}
.contact svg{flex:none;width:16px;height:16px;margin-top:3px}
.links{left:650px;top:1980px;color:#fff;font-size:14.5px}
.links ul{list-style:none;margin-top:10px}
.links li{line-height:24.6px}
.links li.active{color:var(--blue-bright);text-decoration:underline}
.map{left:840px;top:1984px;width:271px;height:169px;background:linear-gradient(135deg,#eef0ec,#f4e6c6 55%,#e9ecef)}
.totop{left:1145px;top:2117px;width:34px;height:34px;border-radius:50%;border:2px solid var(--blue-bright)}
.bottombar{left:0;top:2211px;width:1200px;height:39px;background:var(--green);color:#fff;font-size:15px;display:flex;align-items:center;justify-content:space-between;padding:0 88px}
.bottombar .social i{background:#fff}
.bottombar .social i.on{background:var(--blue)}
</style>
</head>
<body>

<!-- header -->
<div class="abs brand"><span class="brand-dot"></span>TovaLamarpe</div>
<div class="abs topbar">
  <span><svg width="13" height="13" viewBox="0 0 24 24" fill="#4fae3f"><path d="M6.6 10.8a15 15 0 0 0 6.6 6.6l2.2-2.2a1 1 0 0 1 1-.25 11 11 0 0 0 3.6.6 1 1 0 0 1 1 1V20a1 1 0 0 1-1 1A17 17 0 0 1 3 4a1 1 0 0 1 1-1h3.5a1 1 0 0 1 1 1 11 11 0 0 0 .6 3.6 1 1 0 0 1-.25 1z"/></svg>+123-456-7890</span>
  <span><svg width="14" height="12" viewBox="0 0 24 20" fill="#4fae3f"><path d="M2 0h20a2 2 0 0 1 2 2v16a2 2 0 0 1-2 2H2a2 2 0 0 1-2-2V2a2 2 0 0 1 2-2zm10 9L2 3v2l10 6 10-6V3z"/></svg>info@tovalamarpe.com</span>
  <span class="social" aria-label="Social links"><i></i><i class="on"></i><i></i><i></i></span>
</div>
<nav class="abs nav">
  <a class="active">Home</a><a>Therapists</a><a>Organizations</a><a>Videos</a><a>About Us</a><a>Contact Us</a>
</nav>
<a class="abs donate">DONATE</a>
<div class="abs lang">EN <svg width="8" height="5" viewBox="0 0 8 5"><path d="M0 0h8L4 5z" fill="#4fae3f"/></svg></div>

<!-- hero -->
<aside class="abs sidebar">
  <div class="cat active"><svg viewBox="0 0 24 24"><circle cx="12" cy="13" r="5"/><path d="M12 3v3M4 13H2M22 13h-2M5.5 6.5l2 2M18.5 6.5l-2 2M2 20h20"/></svg>Emergency Mental Help
    <svg class="arrow" viewBox="0 0 24 24"><path d="M3 12h17M14 6l6 6-6 6"/></svg></div>
  <div class="cat"><svg viewBox="0 0 24 24"><path d="M3 6h14v10H3zM7 16l-2 4M17 9h4v7h-4"/></svg>Suicide</div>
  <div class="cat two"><svg viewBox="0 0 24 24"><circle cx="9" cy="11" r="5"/><circle cx="15" cy="11" r="5"/><path d="M9 16v5"/></svg>Sexual Assault/Violence<br>Victims</div>
  <div class="cat two"><svg viewBox="0 0 24 24"><path d="M7 12V6a1.5 1.5 0 0 1 3 0v5V4a1.5 1.5 0 0 1 3 0v7V5a1.5 1.5 0 0 1 3 0v9a6 6 0 0 1-12 0v-3a1.5 1.5 0 0 1 3 0"/></svg>Sexual Assault/Violence<br>Assaulters</div>
  <div class="cat"><svg viewBox="0 0 24 24"><circle cx="12" cy="12" r="9"/><circle cx="12" cy="12" r="4"/></svg>Post Trauma</div>
  <div class="cat"><svg viewBox="0 0 24 24"><path d="M5 20v-4a7 7 0 1 1 10 3v1"/><circle cx="11" cy="10" r="3"/></svg>Depression</div>
  <div class="cat"><svg viewBox="0 0 24 24"><circle cx="12" cy="6" r="3"/><path d="M6 21l3-8h6l3 8M4 10l4 3M20 10l-4 3"/></svg>Anxiety</div>
  <div class="cat"><svg viewBox="0 0 24 24"><circle cx="11" cy="8" r="5"/><path d="M4 21h16M8 16l3-3 3 3"/></svg>Addictions</div>
  <div class="cat"><svg viewBox="0 0 24 24"><circle cx="12" cy="12" r="8"/><path d="M8 12h8M12 4v2M12 18v2"/></svg>Sleep Disorders</div>
  <div class="cat"><svg viewBox="0 0 24 24"><path d="M3 13h18a9 9 0 0 1-18 0zM12 4v6M8 6v4M16 6v4"/></svg>Eating Disorders</div>
  <div class="cat"><svg viewBox="0 0 24 24"><circle cx="12" cy="12" r="9"/><path d="M15 9a3 2 0 0 0-6 0c0 3 6 2 6 5a3 2 0 0 1-6 0M12 5v14"/></svg>Financial Problems</div>
  <div class="cat"><svg viewBox="0 0 24 24"><path d="M4 20V10l4-4 4 4v10M12 14l4-3 4 3v6H4"/></svg>Parenthood</div>
  <div class="cat"><svg viewBox="0 0 24 24"><circle cx="8" cy="7" r="3"/><circle cx="16" cy="7" r="3"/><path d="M3 20v-4a5 5 0 0 1 10 0v4M11 20v-4a5 5 0 0 1 10 0v4"/></svg>Relationship</div>
</aside>
<div class="abs hero-photo" role="img" aria-label="Photo of a therapist comforting a patient"></div>
<div class="abs hero-shade"></div>
<h1 class="abs hero-title">EMERGENCY<br>MENTAL HELP</h1>
<p class="abs hero-text">Lorem ipsum dolor sit amet, consectetur adipiscing elit, sed do eiusmod tempor incididunt ut labore et dolore magna aliqua.</p>
<a class="abs hero-btn">MORE OPTIONS FOR EMERGENCY MENTAL HELP</a>

<!-- about -->
<h2 class="abs about-title">ABOUT <em>US</em></h2>
<div class="abs about-text">
  <p>Lorem ipsum dolor sit amet, consectetur adipiscing elit, sed do eiusmod tempor incididunt ut labore et dolore magna aliqua. Ut enim ad minim veniam, quis nostrud exercitation ullamco laboris nisi ut aliquip ex ea commodo consequat.</p>
  <p>Duis aute irure dolor in reprehenderit in voluptate velit esse cillum dolore eu fugiat nulla pariatur. Excepteur sint occaecat cupidatat non proident, sunt in culpa qui officia deserunt mollit anim id est laborum.</p>
</div>
<a class="abs btn blue" style="left:526px;top:908px;width:148px">EXPLORE MORE</a>

<!-- cards -->
<div class="abs card-photo" style="left:88px;top:1024px;background:linear-gradient(120deg,#1c7a55,#b9c3bf 45%,#d8a86a 80%)" role="img" aria-label="Photo of a hand holding a phone with a chat app"></div>
<div class="abs card-box" style="left:112px;top:1245px">
  <h3>SMART CHATLINE</h3>
  <p>Lorem Ipsum is simply dummy text of the printing and typesetting industry. Lorem Ipsum has been the industry's standard dummy text ever since the 1500s...</p>
  <a class="btn green" style="width:143px">EXPLORE MORE</a>
</div>

<div class="abs card-photo" style="left:612px;top:1024px;background:linear-gradient(120deg,#dfe3e6,#c9c4be 55%,#b08a74)" role="img" aria-label="Photo of a therapy session on a sofa"></div>
<div class="abs card-box" style="left:636px;top:1245px">
  <h3>THERAPISTS</h3>
  <p>Lorem Ipsum is simply dummy text of the printing and typesetting industry. Lorem Ipsum has been the industry's standard dummy text ever since the 1500s...</p>
  <a class="btn blue" style="width:156px">FIND THERAPISTS</a>
</div>

<div class="abs card-photo" style="left:88px;top:1452px;background:linear-gradient(120deg,#d8d4d2,#a7958c 55%,#6e6260)" role="img" aria-label="Photo of two people joining hands"></div>
<div class="abs card-box" style="left:112px;top:1670px">
  <h3>ORGANIZATIONS</h3>
  <p>Lorem Ipsum is simply dummy text of the printing and typesetting industry. Lorem Ipsum has been the industry's standard dummy text ever since the 1500s...</p>
  <a class="btn green" style="width:185px">FIND ORGANIZATIONS</a>
</div>

<div class="abs card-photo" style="left:612px;top:1452px;background:linear-gradient(120deg,#e7ecef,#b3bfc6 50%,#2f3236)" role="img" aria-label="Photo of a video call with a therapist on a laptop"></div>
<div class="abs card-box" style="left:636px;top:1670px">
  <h3>VIDEOS</h3>
  <p>Lorem Ipsum is simply dummy text of the printing and typesetting industry. Lorem Ipsum has been the industry's standard dummy text ever since the 1500s...</p>
  <a class="btn green" style="width:143px">VIDEO LIBRARY</a>
</div>

<!-- footer -->
<footer class="abs footer"></footer>
<div class="abs foot-brand"><span class="brand-dot"></span>TovaLamarpe</div>
<div class="abs contact">
  <div class="foot-h">CONATCT INFO</div>
  <ul>
    <li><svg viewBox="0 0 24 24" fill="#4fae3f"><path d="M6.6 10.8a15 15 0 0 0 6.6 6.6l2.2-2.2a1 1 0 0 1 1-.25 11 11 0 0 0 3.6.6 1 1 0 0 1 1 1V20a1 1 0 0 1-1 1A17 17 0 0 1 3 4a1 1 0 0 1 1-1h3.5a1 1 0 0 1 1 1 11 11 0 0 0 .6 3.6 1 1 0 0 1-.25 1z"/></svg>+123-456-7890</li>
    <li><svg viewBox="0 0 24 20" fill="#4fae3f"><path d="M2 0h20a2 2 0 0 1 2 2v16a2 2 0 0 1-2 2H2a2 2 0 0 1-2-2V2a2 2 0 0 1 2-2zm10 9L2 3v2l10 6 10-6V3z"/></svg>info@tovalamarpe.com</li>
    <li><svg viewBox="0 0 24 24" fill="none" stroke="#4fae3f" stroke-width="3"><path d="M12 22s7-7 7-12a7 7 0 0 0-14 0c0 5 7 12 7 12z"/><circle cx="12" cy="10" r="2.5"/></svg>Level 12, 48 Harbour Lane,<br>Perth, WA, 6000</li>
  </ul>
</div>
<div class="abs links">
  <div class="foot-h">QUICK LINK</div>
  <ul>
    <li class="active">Home</li><li>Therapists</li><li>Organizations</li><li>Videos</li><li>About Us</li><li>Contact Us</li>
  </ul>
</div>
<div class="abs map" role="img" aria-label="Map showing the office location"></div>
<div class="abs totop"><svg width="30" height="30" viewBox="0 0 30 30" fill="none" stroke="#2b8de0" stroke-width="2"><path d="M10 9h10M15 23V12M11 16l4-4 4 4"/></svg></div>
<div class="abs bottombar">
  <span>© 2023 TovaLamarpe. All Right Reserved</span>
  <span class="social" aria-label="Social links"><i></i><i class="on"></i><i></i><i></i></span>
</div>

</body>
</html>
```